"Drink Champagne and Dance on the Table" sort of business card needed!

We throw events, weddings, engagement parties, baby showers and the sort of end of year corporate events that people remember long after the glitter has settled - the sort of events that make you stand still and say wow when you walk in and then make you want to "Drink Champagne and Dance on the Tables"

We have a great logo with heaps of potential and need a business card that just screams creative professionals!

We are based in Auckland, NZ and are priced at the Premium end of the market were there are around 10 other main competitors. We need to stand out and make a strong statement about who we are!

Our Business Card will be one of the few items that we print out so are fully prepared to invest in a premium print job.

We really love our logo and think it has heaps of potential! Its ok if you would like to manipulate it (maybe put it on an angle, or use the circle element on its own?).

Black and Gold is very striking, but its very done in our market so we would like to avoid a solid black background please

We have done a bit of an inspiration document to give you an idea of the sort of look and feel we are hoping to achieve.

Target Market(s)

Woman aged 30 - 45 with an income bracket of $70k +

Industry/Entity Type

Event Planning

Contact Information for Business Card

Marnie
hello@fennoriwick.co.nz
www.fennoriwick.co.nz
02734419027

Number of Pages Required

5+ page

Requirements
Must have
• Vibrant colours and design (we love the vibrant pink and gold in the inspiration file)
• We would love to see some colour and creativity (although the black and gold is very striking). Because we are doing such minimal print work I am happy for the cards to be a little more expensive so if you want to use cut outs, rounded corners, gold foil, non standard size etc I am happy for that too. I really want the wow factor.
Nice to have
• We would like the design to be double sided.
Should not have
• The logo colour changed
• Use of Purple or Green or solid black background.
• Wedding Photos!

```html
<!DOCTYPE html>
<html lang="en">
<head>
<meta charset="utf-8">
<title>Fenn and Oriwick – Business Card</title>
<link rel="stylesheet" href="https://fonts.googleapis.com/css2?family=Playfair+Display:wght@700;900&family=Arimo:wght@400&display=swap">
<style>
  :root {
    --stage: #f3ede4;
    --card-white: #ffffff;
    --gold: #c4911f;
    --gold-deep: #a8761a;
    --ink: #141414;
    --champagne: #fff3c4;
    --butter: #f7dc7a;
    --honey: #eabf4e;
    --blush: #f6b8c4;
    --rose-pink: #e9809a;
    --shadow: rgba(80, 50, 20, 0.22);
  }
  * { box-sizing: border-box; margin: 0; padding: 0; }
  html, body {
    width: 1200px; height: 902px; overflow: hidden;
    background: var(--stage);
  }
  .canvas {
    width: 1200px; height: 902px;
    display: flex; align-items: center; justify-content: center; gap: 36px;
  }
  .card {
    position: relative;
    width: 564px; height: 330px;
    overflow: hidden;
    box-shadow: 0 14px 34px var(--shadow);
  }

  /* Brand block, shared */
  .brand {
    display: flex; flex-direction: column; align-items: center;
  }
  .brand-disc {
    border-radius: 50%;
    background: var(--gold);
  }
  .brand-name {
    font-family: "Playfair Display", serif;
    font-weight: 700;
    color: var(--gold);
    white-space: nowrap;
  }
  .brand-tagline {
    display: flex; align-items: center; gap: 8px;
    font-family: "Arimo", sans-serif;
    color: var(--gold);
    letter-spacing: 3px;
    text-transform: uppercase;
    white-space: nowrap;
  }
  .brand-tagline::before,
  .brand-tagline::after {
    content: ""; height: 1px; width: 22px; background: var(--gold);
  }

  /* Back side */
  .card--back {
    background: var(--card-white);
    display: flex; align-items: center; justify-content: center;
  }
  .card--back .brand { gap: 16px; }
  .card--back .brand-disc { width: 104px; height: 104px; }
  .card--back .brand-name { font-size: 38px; line-height: 1; }
  .card--back .brand-tagline { font-size: 12px; margin-top: -6px; }

  /* Front side */
  .card--front { background: var(--champagne); }
  .front-photo {
    position: absolute; inset: 0;
    background:
      radial-gradient(ellipse 20% 12% at 74% 78%, var(--honey) 0%, rgba(234,191,78,0) 100%),
      radial-gradient(ellipse 34% 48% at 27% 52%, #fff6d2 0%, var(--butter) 38%, rgba(247,220,122,0) 78%),
      radial-gradient(ellipse 55% 60% at 10% 95%, var(--blush) 0%, rgba(246,184,196,0) 70%),
      radial-gradient(ellipse 30% 30% at 0% 0%, var(--rose-pink) 0%, rgba(233,128,154,0) 80%),
      linear-gradient(125deg, #fbe6a4 0%, var(--champagne) 55%, #fff8de 100%);
  }
  .front-brand {
    position: absolute; top: 20px; right: 42px;
    gap: 8px;
  }
  .front-brand .brand-disc { width: 66px; height: 66px; }
  .front-brand .brand-name { font-size: 25px; line-height: 1; }
  .front-brand .brand-tagline { font-size: 8px; letter-spacing: 2.5px; }
  .holder-name {
    position: absolute; top: 160px; right: 38px;
    font-family: "Playfair Display", serif; font-weight: 900;
    font-size: 32px; line-height: 1; color: var(--ink);
  }
  .contact-list {
    position: absolute; top: 208px; right: 22px;
    list-style: none;
    font-family: "Arimo", sans-serif; font-size: 15px; line-height: 1; color: var(--ink);
    display: flex; flex-direction: column; align-items: flex-end; gap: 9px;
  }
  .contact-list li { display: flex; align-items: center; gap: 8px; }
  .contact-icon {
    width: 16px; height: 16px; background: var(--ink);
    display: inline-flex; align-items: center; justify-content: center;
    flex: none;
  }
  .contact-icon svg { width: 12px; height: 12px; }
</style>
</head>
<body>
<main class="canvas">
  <section class="card card--back" aria-label="Card back">
    <div class="brand">
      <span class="brand-disc" aria-hidden="true"></span>
      <span class="brand-name">Fenn and Oriwick</span>
      <span class="brand-tagline">Weddings &amp; Events</span>
    </div>
  </section>

  <section class="card card--front" aria-label="Card front">
    <div class="front-photo" role="img" aria-label="Soft-focus pale yellow rose beside two gold rings on a warm cream surface"></div>
    <div class="brand front-brand">
      <span class="brand-disc" aria-hidden="true"></span>
      <span class="brand-name">Fenn and Oriwick</span>
      <span class="brand-tagline">Weddings &amp; Events</span>
    </div>
    <p class="holder-name">Marnie</p>
    <ul class="contact-list">
      <li>02734419027
        <span class="contact-icon" aria-hidden="true">
          <svg viewBox="0 0 12 12"><path d="M3 1.5 L4.8 3.6 L3.9 4.8 Q5 7 7.2 8.1 L8.4 7.2 L10.5 9 L9.4 10.5 Q4.5 10 1.5 2.6 Z" fill="#fff"/></svg>
        </span>
      </li>
      <li>www.fennoriwick.co.nz
        <span class="contact-icon" aria-hidden="true">
          <svg viewBox="0 0 12 12" fill="none" stroke="#fff" stroke-width="1"><circle cx="6" cy="6" r="4.5"/><ellipse cx="6" cy="6" rx="2" ry="4.5"/><line x1="1.5" y1="6" x2="10.5" y2="6"/></svg>
        </span>
      </li>
      <li>hello@fennoriwick.co.nz
        <span class="contact-icon" aria-hidden="true">
          <svg viewBox="0 0 12 12" fill="none" stroke="#fff" stroke-width="1"><rect x="1.5" y="3" width="9" height="6"/><polyline points="1.5,3 6,6.5 10.5,3"/></svg>
        </span>
      </li>
    </ul>
  </section>
</main>
</body>
</html>
```